Brisk Therapy Flyer - Physiotherapy company

I am looking for a two-sided flyer (4"x8") that can be easily posted on cork boards or displayed as needed to provide information about my business. I would like to use the colors found in my logo (see attached) along with white and black. Please have a look at my website for ideas of how I would like the color schemes etc (www.briskcare-demo.ca). I would like it to follow the same style as my website.<br/><br/>FRONT SIDE<br/>I am hoping to have the name of our business "Brisk Therapy" with our slogan "Boreal Physiotherapy - Rehab and Recovery Above the Pines (degrees symbol)" underneath. Somewhere above or around this I would like my logo (see attached). <br/><br/>Below that I would like a title "Services Provided" and then listed: <br/>Mobile Services<br/>Clinic<br/>Telehealth<br/><br/>Below that, I would like another title "Treatments Offered" and then listed: <br/>Hands-on manual therapy<br/>Intramuscular Stimulation (IMS)<br/>Acupuncture<br/>Athletic taping<br/>Injury/condition education<br/>Supervised exercise<br/><br/>Below that I would like "Contact Us":<br/>Brisk Therapy<br/>www.BriskCare-demo.ca<br/>Book online through https://briskcare.bookfake-demo.com/<br/>physio@briskcare-demo.ca<br/>867-555-0148<br/>Direct Billing offered for most extended health providers<br/>(Chatterly, Snapwell logo, kinelogix logo (see attached) on bottom maybe in corner or centered)<br/><br/>BACK SIDE<br/><br/>I would like the logo on there once again maybe. Then I would like these three information sections one on top of the other spaced out appropriately.<br/><br/>Image (needling image) (see attached)<br/>Title: Mobile Physiotherapy<br/>The information below title: If you want to keep moving and need some help, but your current condition makes it difficult or unsafe to travel to and from a clinic to see a physiotherapist, that’s where we come in. We make it easy by offering a mobile service that provides exceptional one-on-one physiotherapy assessment and treatment in the comfort of your own home. There is a small fee to access mobile services. <br/><br/>Image (Hands on knee image) (see attached)<br/>Title: Clinic<br/>The information below title: If you have an injury that is causing you pain or restricting you from doing the activities that you want to do then physiotherapy can help. A traditional approach to physiotherapy where you come to our clinic and we provide one to one education and hands on therapy. <br/><br/>Image (computer, tablet etc) (see attached)<br/>Title: Telehealth<br/>The information below title: If you live outside of Whitehorse or just want easy access to a physiotherapist from the comfort of your home, then Telehealth is for you. Telehealth involves meeting with your physiotherapist using real-time technology, similar to VidLink. Brisk Therapy utilizes Kinelogix for exercise prescription, pain tracking and telehealth. Through Kinelogix or it’s Motivapp you can discuss your treatment plan, diagnoses, exercises, daily activities or any other questions you may have directly with a physiotherapist.<br/><br/><br/><br/>

Industry/Entity Type

Healthcare

Colors

Designer to choose colors to be used in the design.

Requirements
Must have
• Follow the same colors and schemes of my website (www.briskcare-demo.ca)
• Keep it clean and concise
Nice to have
• Images might not fit because I don't want it too cluttered.
Should not have
• Too busy

```html
<!DOCTYPE html>
<html lang="en">
<head>
<meta charset="utf-8">
<title>Brisk Therapy – Services Flyer (Back)</title>
<link rel="stylesheet" href="https://fonts.googleapis.com/css2?family=Source+Sans+3:wght@400;600;700&family=Cinzel:wght@700&display=swap">
<style>
  :root {
    --ink-dark: #2f3133;
    --ink-dark-2: #4a4d50;
    --teal: #2e7f76;
    --teal-deep: #1f5f58;
    --slate: #2b2d30;
    --brand-green: #0f5944;
    --brand-green-text: #1b6b3a;
    --brand-navy: #1e3c64;
    --white: #ffffff;
    --paper: #f2f3f3;
    --social-text: #1e3c64;
  }
  * { margin: 0; padding: 0; box-sizing: border-box; }
  html, body { width: 1200px; height: 2400px; overflow: hidden; background: var(--paper); }
  .flyer {
    position: relative;
    width: 1200px;
    height: 2400px;
    font-family: "Source Sans 3", "Myriad Pro", Arial, sans-serif;
    color: var(--white);
    overflow: hidden;
  }
  .service { position: absolute; left: 0; width: 1200px; overflow: hidden; }
  .service-photo { position: absolute; inset: 0; }
  .service-content { position: relative; text-align: center; }
  .service-title {
    font-weight: 600;
    font-size: 40px;
    letter-spacing: 0.5px;
    line-height: 1;
  }
  .service-text { margin: 0 auto; }

  .service--mobile { top: 0; height: 696px; }
  .service--mobile .service-photo {
    background: radial-gradient(ellipse at 45% 40%, #6c6f72 0%, #4b4e51 45%, #2f3133 100%);
  }
  .service--mobile .service-title { padding-top: 148px; }
  .service--mobile .service-text {
    width: 1040px;
    margin-top: 40px;
    font-size: 35px;
    line-height: 58.5px;
    letter-spacing: 1.6px;
    text-align: justify;
    text-align-last: center;
  }

  .service--clinic { top: 696px; height: 608px; }
  .service--clinic .service-photo {
    background: radial-gradient(ellipse at 40% 30%, #3f8f86 0%, #2e7f76 45%, #1f5f58 100%);
  }
  .service--clinic .service-title { padding-top: 113px; }
  .service--clinic .service-text {
    width: 1060px;
    margin-top: 40px;
    font-size: 34px;
    line-height: 58px;
  }

  .service--telehealth { top: 1304px; height: 648px; }
  .service--telehealth .service-photo {
    background: linear-gradient(180deg, #3a3c3f 0%, #2b2d30 55%, #232527 100%);
  }
  .service--telehealth .service-title { padding-top: 97px; }
  .service--telehealth .service-text {
    width: 1120px;
    margin-top: 22px;
    font-size: 30.5px;
    line-height: 58px;
    text-align: justify;
    text-align-last: center;
  }

  .contact {
    position: absolute;
    top: 1952px; left: 0;
    width: 1200px; height: 448px;
    background: var(--paper);
  }
  .brand-mark {
    position: absolute;
    left: 64px; top: 40px;
    width: 230px;
    text-align: center;
    color: var(--brand-navy);
    font-family: "Source Sans 3", Arial, sans-serif;
    font-weight: 700;
  }
  .brand-mark-square {
    width: 110px; height: 110px;
    margin: 0 auto 18px;
    background: var(--brand-navy);
  }
  .brand-mark-name { font-size: 40px; line-height: 1; letter-spacing: 1px; }

  .book-pill {
    position: absolute;
    left: 384px; top: 27px;
    width: 603px; height: 64px;
    border-radius: 32px;
    background: var(--brand-green);
    color: var(--white);
    font-size: 39px;
    font-weight: 600;
    line-height: 64px;
    padding-left: 40px;
  }
  .contact-lines {
    position: absolute;
    left: 395px; top: 108px;
    list-style: none;
    color: var(--brand-green-text);
    font-size: 38px;
    font-weight: 600;
    line-height: 52px;
  }

  .social-row {
    position: absolute;
    left: 0; top: 360px;
    width: 1200px;
    height: 64px;
  }
  .social-item {
    position: absolute;
    top: 0;
    display: flex;
    align-items: center;
    height: 64px;
    font-size: 38px;
    font-weight: 600;
    color: var(--social-text);
  }
  .social-dot {
    width: 56px; height: 56px;
    border-radius: 50%;
    background: var(--brand-navy);
    margin-right: 14px;
  }
  .social-item--chatterly { left: 40px; }
  .social-item--snapwell { left: 478px; }
  .social-item--motivapp { left: 872px; color: var(--teal); font-size: 50px; }
  .social-square {
    width: 44px; height: 44px;
    background: var(--teal);
    margin-right: 12px;
  }
</style>
</head>
<body>
<main class="flyer">

  <section class="service service--mobile">
    <div class="service-photo" role="img" aria-label="Photo of a physiotherapist performing needling treatment on a patient's shoulder, darkened"></div>
    <div class="service-content">
      <h2 class="service-title">MOBILE PHYSIOTHERAPY</h2>
      <p class="service-text">If you want to keep moving and need some help, but your current condition makes it difficult or unsafe to travel to and from a clinic to see a physiotherapist, that’s where we come in. We make it easy by offering a mobile service that provides exceptional one-on-one physiotherapy assessment and treatment in the comfort of your own home. There is a small fee to access mobile services.</p>
    </div>
  </section>

  <section class="service service--clinic">
    <div class="service-photo" role="img" aria-label="Photo of a therapist's hands treating a patient's knee, tinted teal"></div>
    <div class="service-content">
      <h2 class="service-title">CLINIC</h2>
      <p class="service-text">The information below title: If you have an injury that is causing you pain or restricting you from doing the activities that you want to do then physiotherapy can help. A traditional approach to physiotherapy where you come to our clinic and we provide one to one education and hands on therapy.</p>
    </div>
  </section>

  <section class="service service--telehealth">
    <div class="service-photo" role="img" aria-label="Photo of a laptop, tablet and phone showing an exercise app and video call, darkened"></div>
    <div class="service-content">
      <h2 class="service-title">TELEHEALTH</h2>
      <p class="service-text">If you live outside of Whitehorse or just want easy access to a physiotherapist from the comfort of your home, then Telehealth is for you. Telehealth involves meeting with your physiotherapist using real-time technology, similar to VidLink. Brisk Therapy utilizes Kinelogix for exercise prescription, pain tracking and telehealth. Through Kinelogix or it’s Motivapp you can discuss your treatment plan, diagnoses, exercises, daily activities or any other questions you may have directly with a physiotherapist.</p>
    </div>
  </section>

  <footer class="contact">
    <div class="brand-mark">
      <div class="brand-mark-square"></div>
      <div class="brand-mark-name">BRISK<br>THERAPY</div>
    </div>

    <div class="book-pill">BOOK ONLINE THROUGH</div>
    <ul class="contact-lines">
      <li>https://briskcare.bookfake-demo.com</li>
      <li>physio@briskcare-demo.ca</li>
      <li>867-555-0148</li>
    </ul>

    <div class="social-row">
      <div class="social-item social-item--chatterly"><span class="social-dot"></span>Brisk Therapy</div>
      <div class="social-item social-item--snapwell"><span class="social-dot"></span>BriskTherapy</div>
      <div class="social-item social-item--motivapp"><span class="social-square"></span>Motivapp</div>
    </div>
  </footer>

</main>
</body>
</html>
```